Trifold - Gentle Horizon Therapy

Marianne Dobbs, Psy.D.Licensed Psychologist

this is for hypnosis and meditation
I like decorative font for my name (conservative decorative)

calming effect is most imortant

Target Market(s)

clients with depression, pain, anxiety - adults and aged

Industry/Entity Type

Conservative

Font styles to use
Serif

Colors
abd037
85cae6
cadf82
34a7d7
ffffff
886aae
6b449b

Requirements
Must have
• I like zen-like calming effects. lime Green, light blues and purple. I like waves and color.
• I like water and light, flowers and plants - bamboo, stacking rocks, ocean, water, lotus flowers
Should not have
• not too much purple
• Mostly green and blue

```html
<!DOCTYPE html>
<html lang="en">
<head>
<meta charset="utf-8">
<title>Gentle Horizon Therapy – Trifold</title>
<link href="https://fonts.googleapis.com/css2?family=Tinos:ital,wght@0,400;0,700;1,400;1,700&display=swap" rel="stylesheet">
<style>
:root{
  --lime:#abd037;
  --lime-deep:#8cbf2a;
  --lime-soft:#cadf82;
  --teal:#1aa8a2;
  --teal-deep:#138f8c;
  --aqua:#34b3b0;
  --sky:#85cae6;
  --blue:#34a7d7;
  --violet:#886aae;
  --ink:#2f3b3b;
  --grey:#5b6666;
  --paper:#ffffff;
  --stage:#e6e6e6;
}
*{box-sizing:border-box;margin:0;padding:0}
html,body{width:1200px;height:2400px;overflow:hidden}
body{background:var(--stage);font-family:"Tinos",serif;color:var(--ink)}
.spread{position:absolute;left:45px;width:1110px;height:858px;display:flex;box-shadow:0 10px 30px rgba(0,0,0,.18);background:var(--paper)}
.spread--outside{top:170px}
.spread--inside{top:1270px}
.panel{position:relative;width:370px;height:858px;overflow:hidden}
.panel + .panel{border-left:1px solid rgba(0,0,0,.06)}
.layer{position:absolute;left:0;top:0;width:370px;height:858px}
.abs{position:absolute}
.phone-icon{width:16px;height:16px;vertical-align:-2px;margin-right:6px}

/* outside: services */
.services{background:var(--paper)}
.services__title{left:34px;top:78px;font-size:24px;font-style:italic;color:var(--teal)}
.services__list{left:34px;top:122px;width:300px;list-style:none}
.service{margin-bottom:18px}
.service__name{font-size:14px;font-weight:700;color:var(--teal-deep);display:flex;align-items:center;gap:8px}
.service__name::before{content:"";width:9px;height:9px;border-radius:50%;background:var(--lime)}
.service__text{font-size:12.5px;line-height:1.45;color:var(--grey);margin-top:3px}
.services__note{left:34px;top:720px;width:300px;font-size:12px;font-style:italic;color:var(--grey)}
.band-phone{left:0;bottom:0;width:370px;height:46px;color:var(--paper);font-size:16px;display:flex;align-items:center;padding-left:34px}

/* outside: back */
.back__name{left:0;top:30px;width:370px;text-align:center;color:var(--paper);font-size:24px;font-weight:700}
.back__role{left:0;top:62px;width:370px;text-align:center;color:var(--paper);font-size:17px;font-style:italic}
.brand{display:flex;flex-direction:column;align-items:center;gap:10px}
.brand__dot{width:44px;height:44px;border-radius:50%}
.brand__name{font-size:27px;letter-spacing:6px;text-transform:uppercase}
.back__brand{left:0;top:215px;width:370px;color:var(--paper)}
.back__brand .brand__dot{background:var(--paper)}
.back__motto{left:0;top:360px;width:370px;text-align:center;color:var(--paper);font-size:25px;font-style:italic;font-weight:700;line-height:1.5}
.back__address{left:0;top:520px;width:370px;text-align:center;color:var(--paper);font-size:17px;line-height:1.5}
.back__web{left:0;bottom:18px;width:370px;text-align:center;color:var(--paper);font-size:15px;letter-spacing:.5px}

/* outside: cover */
.cover__brand{left:0;top:38px;width:370px;color:var(--lime-deep)}
.cover__brand .brand__dot{background:var(--lime)}
.cover__text{right:28px;top:588px;width:320px;text-align:right}
.cover__name,.cover__line{font-size:21px;font-weight:700;color:var(--ink);line-height:1.3}
.cover__tag{margin-top:10px;font-size:20px;font-style:italic;color:var(--teal);line-height:1.3}
.cover__spec{margin-top:8px;font-size:14.5px;color:var(--grey)}

/* inside: left */
.ght{background:var(--lime)}
.ght__title{left:28px;top:350px;width:320px;font-size:17px;font-weight:700;color:var(--paper)}
.ght__text{left:28px;top:382px;width:318px;font-size:13px;line-height:1.5;color:var(--paper)}
.ght__lead{left:28px;top:560px;width:318px;font-size:13.5px;color:var(--paper);font-style:italic}
.ght__list{left:46px;top:588px;width:300px;font-size:14px;line-height:1.6;color:var(--paper)}

/* inside: middle */
.session__head{left:24px;top:34px;width:322px;text-align:center;font-size:17px;font-weight:700;color:var(--teal);line-height:1.3;text-transform:uppercase}
.session__text{left:26px;width:318px;font-size:12.5px;line-height:1.5;color:var(--grey)}
.session__sub{left:26px;width:318px;font-size:16px;font-weight:700;font-style:italic;color:var(--teal)}
.session__list{left:44px;top:690px;width:300px;font-size:13px;line-height:1.5;color:var(--grey)}
.session__band{left:0;bottom:0;width:370px;height:44px;background:var(--teal);color:var(--paper);font-size:16px;display:flex;align-items:center;justify-content:center}

/* inside: right */
.bio{background:linear-gradient(180deg,var(--teal-deep),var(--aqua) 60%,#5cc0a0)}
.bio__head{left:28px;top:30px;font-size:24px;font-weight:700;color:var(--paper);display:flex;align-items:center;gap:10px}
.bio__head::before{content:"";width:22px;height:22px;border-radius:50%;background:var(--paper)}
.bio__text{left:28px;width:314px;font-size:12.5px;line-height:1.5;color:var(--paper)}
.portrait{left:214px;top:560px;width:130px;height:130px;border-radius:50%;border:5px solid var(--paper);background:radial-gradient(circle at 50% 40%,#e9d3b8,#a9cde0 70%)}
</style>
</head>
<body>

<!-- OUTSIDE -->
<section class="spread spread--outside">

  <div class="panel services">
    <svg class="layer" viewBox="0 0 370 858">
      <path d="M0 0H370V40Q200 70 0 30Z" fill="var(--lime-soft)"/>
      <path d="M0 770Q190 740 370 790V858H0Z" fill="var(--lime)"/>
      <path d="M0 795Q190 770 370 812V858H0Z" fill="var(--teal)"/>
    </svg>
    <h2 class="abs services__title">Psychological Services</h2>
    <ul class="abs services__list">
      <li class="service"><p class="service__name">Initial Evaluation</p><p class="service__text">Mental health assessment, diagnosis and care planning with clear next steps.</p></li>
      <li class="service"><p class="service__name">Gentle Horizon Therapy (GHT)</p><p class="service__text">A gentle approach that eases stored emotion and trauma, helping the mind release old patterns quietly.</p></li>
      <li class="service"><p class="service__name">Mindfulness Meditation</p><p class="service__text">Guided breathing and stillness practice for calm, focus and steady emotional balance.</p></li>
      <li class="service"><p class="service__name">Hypnosis for Relief</p><p class="service__text">Relaxed focused states used to ease pain, worry, sleep trouble and tension.</p></li>
      <li class="service"><p class="service__name">Meditation for Wellness</p><p class="service__text">Personalized meditation for calm, healing and well-being.</p></li>
    </ul>
    <p class="abs services__note">Sessions available for adults and older adults.</p>
    <p class="abs band-phone"><svg class="phone-icon" viewBox="0 0 24 24"><path fill="#fff" d="M6.6 10.8a15 15 0 006.6 6.6l2.2-2.2a1 1 0 011-.25 11.4 11.4 0 003.6.57 1 1 0 011 1V20a1 1 0 01-1 1A17 17 0 013 4a1 1 0 011-1h3.5a1 1 0 011 1 11.4 11.4 0 00.57 3.6 1 1 0 01-.25 1z"/></svg>555 014-2286</p>
  </div>

  <div class="panel back">
    <div class="layer" role="img" aria-label="Photo of calm turquoise water" style="background:linear-gradient(180deg,#5fc3a8 0%,#27a89f 40%,#1a9a8e 70%,#67b94a 100%)"></div>
    <svg class="layer" viewBox="0 0 370 858">
      <path d="M0 0H370V95Q190 130 0 100Z" fill="var(--lime)"/>
      <path d="M0 100Q190 130 370 95V108Q190 145 0 112Z" fill="var(--lime-soft)"/>
      <path d="M0 815Q190 800 370 820V858H0Z" fill="var(--lime)"/>
    </svg>
    <p class="abs back__name">Marianne Dobbs, Psy.D.</p>
    <p class="abs back__role">Licensed Psychologist</p>
    <div class="abs brand back__brand"><span class="brand__dot"></span><span class="brand__name">Serene Shore</span></div>
    <p class="abs back__motto">Heal the Past<br>Embrace the Present<br>Create the Future</p>
    <p class="abs back__address">Harbor Plaza<br>418 Ocean Way #12<br>Seabright, FL 32900<br>555 014-2286</p>
    <p class="abs back__web">www.sereneshorewellness.com</p>
  </div>

  <div class="panel cover">
    <svg class="layer" viewBox="0 0 370 858">
      <path d="M0 165Q180 120 370 175V200Q180 150 0 195Z" fill="var(--lime)"/>
      <path d="M0 200Q180 160 370 205V212Q180 172 0 212Z" fill="var(--teal)"/>
      <path d="M0 790Q190 770 370 780V858H0Z" fill="var(--lime)"/>
      <path d="M0 808Q190 790 370 800V858H0Z" fill="var(--teal)"/>
    </svg>
    <svg class="layer" viewBox="0 0 370 858" role="img" aria-label="Photo of a violet lotus flower with a yellow centre">
      <defs><radialGradient id="lotus" cx="50%" cy="45%" r="60%"><stop offset="0" stop-color="#e7c53a"/><stop offset=".22" stop-color="#9c7fcf"/><stop offset=".6" stop-color="#6d55a8"/><stop offset="1" stop-color="#2f5a2c"/></radialGradient></defs>
      <path d="M70 230Q200 195 370 220V555Q250 575 150 560Q80 480 70 230Z" fill="url(#lotus)"/>
    </svg>
    <svg class="layer" viewBox="0 0 370 858">
      <path d="M120 575Q250 540 370 545V552Q250 552 120 580Z" fill="var(--lime)"/>
    </svg>
    <div class="abs brand cover__brand"><span class="brand__dot"></span><span class="brand__name">Serene Shore</span></div>
    <div class="abs cover__text">
      <p class="cover__name">Marianne Dobbs, Psy.D.</p>
      <p class="cover__line">Live Well, Love Well</p>
      <p class="cover__line">Licensed Psychologist</p>
      <p class="cover__tag">Unleashing the Power of the Mind for Healing and Well-being</p>
      <p class="cover__spec">Specializing in Adults &amp; Gentle Horizon Therapy</p>
    </div>
    <p class="abs band-phone" style="justify-content:center;padding-left:0"><svg class="phone-icon" viewBox="0 0 24 24"><path fill="#fff" d="M6.6 10.8a15 15 0 006.6 6.6l2.2-2.2a1 1 0 011-.25 11.4 11.4 0 003.6.57 1 1 0 011 1V20a1 1 0 01-1 1A17 17 0 013 4a1 1 0 011-1h3.5a1 1 0 011 1 11.4 11.4 0 00.57 3.6 1 1 0 01-.25 1z"/></svg>555 014-2286</p>
  </div>
</section>

<!-- INSIDE -->
<section class="spread spread--inside">

  <div class="panel ght">
    <div class="abs" role="img" aria-label="Photo of a dandelion seed head against a blue sky" style="left:0;top:0;width:370px;height:330px;background:radial-gradient(circle at 55% 55%,#f4f6f2 0,#cfe3ef 22%,#4a8fc9 60%,#1f5fa8 100%)"></div>
    <svg class="layer" viewBox="0 0 370 858">
      <path d="M0 300Q190 250 370 290V330Q190 300 0 340Z" fill="var(--paper)" opacity=".9"/>
      <path d="M0 320Q190 285 370 312V858H0Z" fill="var(--lime)"/>
    </svg>
    <h3 class="abs ght__title">What is Gentle Horizon Therapy (GHT)?</h3>
    <p class="abs ght__text">GHT effectively addresses mental health and emotional issues in a short time. It works directly with the part of the mind that holds fear and pain, so lasting relief can come gently, often within a few sessions, without reliving past events.</p>
    <p class="abs ght__lead">GHT is effective for many of life's problems including:</p>
    <ul class="abs ght__list">
      <li>PTSD, Sexual Abuse and Childhood Abuse</li>
      <li>Grief, Infidelity and Heartbreak</li>
      <li>Relationship Issues</li>
      <li>Anger and Resentment</li>
      <li>Guilt / Shame</li>
      <li>Anxiety / Fear</li>
      <li>Nightmares / Insomnia</li>
      <li>Stress related symptoms and Pain</li>
    </ul>
  </div>

  <div class="panel session">
    <svg class="layer" viewBox="0 0 370 858">
      <path d="M0 780Q190 740 370 770V814H0Z" fill="var(--lime)"/>
    </svg>
    <h3 class="abs session__head">Clearing Old Stuff and<br>Making Way for New Beginnings</h3>
    <p class="abs session__text" style="top:96px">If you have been unable to let go of painful memories, it is likely that you are still carrying the emotional weight of those moments. Even when we understand what happened, the feelings can stay stuck and shape the way we think, rest and relate to others. GHT helps the mind gently clear this weight, so that what once felt heavy becomes a memory without the pain, opening room for calm and new beginnings.</p>
    <h4 class="abs session__sub" style="top:322px">What happens in a GHT Session?</h4>
    <p class="abs session__text" style="top:350px">Trauma is stored in the mind and body. In GHT you will experience a calm, relaxed state while we talk together about what is troubling you. Using guided imagery, gentle language and soothing metaphors, the mind is invited to release old patterns. You stay aware and in control throughout, and many people notice a deep sense of peace and lightness at the end of each session.</p>
    <h4 class="abs session__sub" style="top:660px">Clear Your Mind and Change Your World</h4>
    <ul class="abs session__list">
      <li>Discover and resolve hidden causes for emotional difficulties</li>
      <li>Eliminate unconscious conflicts blocking desired change</li>
      <li>Promote mind / body healing</li>
    </ul>
    <p class="abs session__band"><svg class="phone-icon" viewBox="0 0 24 24"><path fill="#fff" d="M6.6 10.8a15 15 0 006.6 6.6l2.2-2.2a1 1 0 011-.25 11.4 11.4 0 003.6.57 1 1 0 011 1V20a1 1 0 01-1 1A17 17 0 013 4a1 1 0 011-1h3.5a1 1 0 011 1 11.4 11.4 0 00.57 3.6 1 1 0 01-.25 1z"/></svg>555 014-2286</p>
  </div>

  <div class="panel bio">
    <div class="abs" role="img" aria-label="Photo of green bamboo stems reflected in still water" style="left:0;top:560px;width:370px;height:298px;background:linear-gradient(180deg,#8fcf6a 0%,#cfe8a6 45%,#f1f7e4 100%)"></div>
    <svg class="layer" viewBox="0 0 370 858">
      <path d="M0 520Q180 600 370 540V600Q180 640 0 580Z" fill="var(--lime)" opacity=".85"/>
      <path d="M0 560Q180 630 370 575V600Q180 650 0 600Z" fill="var(--paper)" opacity=".7"/>
    </svg>
    <h3 class="abs bio__head">Dr. Marianne Dobbs</h3>
    <p class="abs bio__text" style="top:80px">Dr. Dobbs is a licensed clinical psychologist specializing in the treatment of anxiety, depression, chronic pain and the emotional effects of trauma in adults and older adults.</p>
    <p class="abs bio__text" style="top:170px">She has over 20 years of clinical experience in private practice, hospital and community settings, and has completed advanced training in hypnosis, meditation and Gentle Horizon Therapy.</p>
    <p class="abs bio__text" style="top:275px">She earned her doctorate in clinical psychology and has taught and supervised therapists throughout her career, sharing a calm and compassionate approach to care.</p>
    <p class="abs bio__text" style="top:375px">She will collaborate with you to create solutions for healing, empowerment and wellness.</p>
    <div class="abs portrait" role="img" aria-label="Portrait photo of Dr. Marianne Dobbs"></div>
  </div>
</section>

</body>
</html>
```